Wedding Invite Location

We had my daughter's wedding invitations printed and mailed out before realizing we forgot to put the location of the wedding on the invitation. We would like to send out a postcard with the location to all who received an invitation

The pertinent information:

Bethany Morrow and Gregory Sadowin

Grace Fellowship Chapel
24650 Melbrook Rd.
St. Clair Shores, MI 48237

Reception immediately following the service on the church grounds

```html
<!DOCTYPE html>
<html lang="en">
<head>
<meta charset="UTF-8">
<title>Wedding Location Postcard</title>
<link rel="stylesheet" href="https://fonts.googleapis.com/css2?family=Josefin+Sans:wght@400&family=Parisienne&display=swap">
<style>
  :root {
    --backdrop: #e4e4e7;
    --card: #ffffff;
    --band: #4a4749;
    --accent: #f2a19c;
    --ink-light: #ffffff;
    --rule: #b9b9bb;
    --sand-light: #dcdcde;
    --sand-mid: #b7b8bb;
    --sand-dark: #8d8e92;
    --dress: #f2776a;
  }
  * { box-sizing: border-box; margin: 0; padding: 0; }
  html, body { width: 1200px; height: 900px; overflow: hidden; }
  body {
    background: var(--backdrop);
    position: relative;
    font-family: "Josefin Sans", sans-serif;
  }
  .postcard {
    position: absolute;
    background: var(--card);
    box-shadow: 0 2px 10px rgba(0,0,0,0.18);
  }

  /* Front */
  .postcard-front { left: 110px; top: 150px; width: 440px; height: 590px; }
  .engagement-photo {
    position: absolute; left: 14px; top: 14px; right: 14px; bottom: 14px;
    border-radius: 18px;
    background:
      radial-gradient(ellipse 22% 18% at 64% 50%, var(--dress) 0%, rgba(242,119,106,0) 100%),
      radial-gradient(ellipse 20% 24% at 38% 50%, #c9a9aa 0%, rgba(201,169,170,0) 100%),
      radial-gradient(ellipse at 50% 55%, var(--sand-light) 0%, var(--sand-mid) 70%, var(--sand-dark) 100%);
    box-shadow: inset 0 0 22px 10px rgba(255,255,255,0.85);
  }
  .front-band {
    position: absolute; left: 0; right: 0; top: 40px; height: 126px;
    background: var(--band);
    display: flex; flex-direction: column; align-items: center; justify-content: center;
    gap: 6px;
  }

  .monogram {
    width: 86px; height: 66px;
    border-radius: 50%;
    background: radial-gradient(ellipse at center, rgba(255,255,255,0.35) 0%, rgba(255,255,255,0.08) 70%, rgba(255,255,255,0) 100%);
  }
  .couple-names {
    font-family: "Parisienne", cursive;
    color: var(--ink-light);
    font-size: 17px;
    white-space: nowrap;
  }

  /* Back */
  .postcard-back { left: 610px; top: 235px; width: 540px; height: 420px; }
  .details-panel {
    position: absolute; left: 0; top: 0; width: 243px; height: 340px;
    background: var(--band);
    border-right: 9px solid var(--accent);
    color: var(--ink-light);
    text-align: center;
    padding: 30px 14px 0;
  }
  .details-title {
    font-family: "Parisienne", cursive;
    font-weight: 400;
    font-size: 33px;
    line-height: 1;
    margin-bottom: 12px;
  }
  .venue-address { font-style: normal; font-size: 14.5px; line-height: 1.4; }
  .reception-note { font-size: 12.5px; line-height: 1.5; margin-top: 14px; }
  .details-signoff {
    position: absolute; left: 0; right: 0; bottom: 14px;
    display: flex; flex-direction: column; align-items: center; gap: 4px;
  }
  .details-signoff .couple-names { font-size: 15px; }

  .stamp-box {
    position: absolute; right: 30px; top: 28px; width: 88px; height: 88px;
    border: 1px solid var(--rule);
  }
  .address-lines { position: absolute; left: 290px; top: 192px; }
</style>
</head>
<body>

<section class="postcard postcard-front" aria-label="Postcard front">
  <div class="engagement-photo" role="img" aria-label="Engagement photo of the couple on a sandy beach, holding red roses and reaching up toward the camera"></div>
  <div class="front-band">
    <div class="monogram" role="img" aria-label="Script monogram of the couple's initials with red roses"></div>
    <p class="couple-names">Bethany Morrow &amp; Gregory Sadowin</p>
  </div>
</section>

<section class="postcard postcard-back" aria-label="Postcard back">
  <div class="details-panel">
    <h1 class="details-title">Wedding Place</h1>
    <address class="venue-address">
      Grace Fellowship Chapel<br>
      24650 Melbrook Rd.<br>
      St. Clair Shores, MI 48237
    </address>
    <p class="reception-note">Reception immediately following the<br>service on the church grounds</p>
    <div class="details-signoff">
      <div class="monogram" role="img" aria-label="Script monogram of the couple's initials"></div>
      <p class="couple-names">Bethany Morrow &amp; Gregory Sadowin</p>
    </div>
  </div>
  <div class="stamp-box" aria-hidden="true"></div>
  <svg class="address-lines" width="202" height="125" viewBox="0 0 202 125" aria-hidden="true">
    <g stroke="#b9b9bb" stroke-width="1">
      <line x1="0" y1="0.5" x2="202" y2="0.5"/>
      <line x1="0" y1="24.5" x2="202" y2="24.5"/>
      <line x1="0" y1="48.5" x2="202" y2="48.5"/>
      <line x1="0" y1="72.5" x2="202" y2="72.5"/>
      <line x1="0" y1="96.5" x2="202" y2="96.5"/>
      <line x1="0" y1="120.5" x2="202" y2="120.5"/>
    </g>
  </svg>
</section>

</body>
</html>
```